Organic Herbs & Spices container

Greek startup company, which cultivate and trade spices and herbs (such as oregano, mint, thyme, sage etc.)

At present we are interested in only the type and shape of packaging which should be made by materials such as paper, cardboard, laminated paper and others based on paper or plastic.

Package size vary from 80g (2.82oz) - 300g (10.58oz). We are going to use the same packing for a variety of products with different information

* Please find attached our logo which should be included in the design.
* There is no company name available at the moment, however a name placeholder should be included.
* include a placeholder for the type of product (sage, oregano, mint, tea etc...).
* Each package should have a place in order to include product details and nutrition facts.

e.g.
xxxx (company name placeholder)
Sage (product type)
product details and nutrition facts.
Updates

Dear designers,first of all, thank you for your proposals. Please find bellow some updates for the project.- It is mandatory to include the logo into the design - Each package should be able to stored vertically - We are looking for one specific package design, please do not submit many variations of a certain package neither colour differentiations Thanks and good luck Added Wednesday, September 28, 2016

Please avoid the use of images. The same package will be used for all the kinds of products (only name and maybe colour will be different among different products. A transparent frame that will show the contents could be used too) Added Wednesday, September 28, 2016

Please find attached logo in EPS format

Our logo is the baseline, any concepts should be based on it. Try to avoid just adding the logo as a small sticker somewhere on the design. Please try to create around it at any way toy like. This could be, to visualize it as a 3D shape or object which can be used as the container of the products.

Reason: We would like to extend the time of the project. We believe that most of the submitted designs do not comply with our requirements.

Reason: We would like to see a bigger variety of ideas

Target Market(s)

Pretty much to anyone over 20 years old worldwide.

Industry/Entity Type

Nutrition

Requirements
Must have
• It should be attractive, easily recognized, simple yet innovative, durable, functional (easy to use) and easy to store.
Should not have
• Project must not include complex or obnoxious shapes and colours.

```html
<!DOCTYPE html>
<html lang="en">
<head>
<meta charset="utf-8">
<title>Sage Organic Herbs – Pouch Front</title>
<link rel="stylesheet" href="https://fonts.googleapis.com/css2?family=Belleza&family=Tinos:wght@400;700&display=swap">
<style>
  :root {
    --backdrop: #f1f1f1;
    --kraft: #b48f6d;
    --kraft-edge: #a88363;
    --label-black: #050505;
    --ink-white: #fbf8f4;
    --rule-white: rgba(255, 255, 255, 0.85);
    --mark-green: #6a9a2c;
    --illustration-core: rgba(246, 238, 228, 0.55);
    --illustration-fade: rgba(246, 238, 228, 0);
  }
  * { margin: 0; padding: 0; box-sizing: border-box; }
  html, body {
    width: 1200px;
    height: 1200px;
    overflow: hidden;
    background: var(--backdrop);
  }
  .canvas {
    position: relative;
    width: 1200px;
    height: 1200px;
    background: var(--backdrop);
  }
  .pouch-front {
    position: absolute;
    left: 320px;
    top: 135px;
    width: 550px;
    height: 950px;
    background: var(--kraft);
    border: 1px solid var(--kraft-edge);
    border-radius: 10px 10px 4px 4px;
    color: var(--ink-white);
  }
  .brand-label {
    position: absolute;
    left: 160px;
    top: 0;
    width: 220px;
    height: 250px;
    background: var(--label-black);
  }
  .brand-dot {
    position: absolute;
    left: 82px;
    top: 70px;
    width: 56px;
    height: 56px;
    border-radius: 50%;
    background: var(--mark-green);
  }
  .brand-name {
    position: absolute;
    left: 0;
    top: 187px;
    width: 100%;
    text-align: center;
    font-family: "Belleza", sans-serif;
    font-size: 13.5px;
    font-weight: 700;
    letter-spacing: 1.6px;
    color: var(--ink-white);
  }
  .herb-illustration {
    position: absolute;
    left: 205px;
    top: 330px;
    width: 130px;
    height: 150px;
    background: radial-gradient(ellipse at 50% 50%, var(--illustration-core) 0%, var(--illustration-core) 35%, var(--illustration-fade) 72%);
  }
  .product-name {
    position: absolute;
    left: 0;
    top: 484px;
    width: 542px;
    text-align: center;
    font-family: "Belleza", sans-serif;
    font-weight: 400;
    font-size: 108px;
    line-height: 1;
    letter-spacing: 1px;
  }
  .product-line {
    position: absolute;
    left: 0;
    top: 584px;
    width: 545px;
    text-align: center;
    font-family: "Belleza", sans-serif;
    font-size: 23px;
    letter-spacing: 3px;
    font-weight: 700;
  }
  .benefit-list {
    position: absolute;
    left: 162px;
    top: 664px;
    width: 216px;
    height: 106px;
    list-style: none;
    border-left: 1px solid var(--rule-white);
    font-family: "Belleza", sans-serif;
    font-size: 17px;
    letter-spacing: 0.4px;
  }
  .benefit-list li {
    height: 35px;
    line-height: 38px;
    padding-left: 22px;
    white-space: nowrap;
  }
  .benefit-list li + li {
    border-top: 1px solid var(--rule-white);
  }
  .net-weight {
    position: absolute;
    left: 269px;
    top: 796px;
    font-family: "Tinos", serif;
    font-size: 17px;
    letter-spacing: 1px;
  }
  .net-weight strong { font-weight: 700; }
</style>
</head>
<body>
  <main class="canvas">
    <section class="pouch-front">
      <div class="brand-label">
        <span class="brand-dot"></span>
        <p class="brand-name">COMPANY NAME</p>
      </div>

      <div class="herb-illustration" role="img" aria-label="White line illustration of a flowering sage sprig"></div>

      <h1 class="product-name">SAGE</h1>
      <p class="product-line">ORGANIC HERBS</p>

      <ul class="benefit-list">
        <li>Bone Strength</li>
        <li>Cognitive Boost</li>
        <li>Immune System Strength</li>
      </ul>

      <p class="net-weight"><strong>80g</strong> (2.82oz)</p>
    </section>
  </main>
</body>
</html>
```